Fernvale Business Card Design

We are looking for a fresh business card design for our new logo. We would like a business card that is unique but friendly. We are in the window coverings business offering blinds, shutters and shades for homes.

Target Market(s)

Targeting the end-consumer

Industry/Entity Type

Business

Requirements
Must have
• Must have a dedicates space for a photo of our sales person. Must contain our new logo (attached).

```html
<!DOCTYPE html>
<html lang="en">
<head>
<meta charset="UTF-8">
<title>Fernvale Business Card</title>
<link rel="stylesheet" href="https://fonts.googleapis.com/css2?family=Lato:wght@400;700&family=Oswald:wght@500&display=swap">
<style>
  :root {
    --backdrop: #2e2e30;
    --green-deep: #7cc242;
    --green-light: #a9d66e;
    --green-ink: #8cc63f;
    --paper: #ffffff;
    --paper-shade: #f1f1f1;
    --photo-top: #e4efd8;
    --photo-bottom: #c9dfb2;
  }
  html, body {
    margin: 0;
    padding: 0;
    width: 1200px;
    height: 791px;
    overflow: hidden;
    background: var(--backdrop);
  }
  .canvas {
    position: relative;
    width: 1200px;
    height: 791px;
  }
  .card {
    position: absolute;
    width: 600px;
    height: 340px;
    border-radius: 2px;
    box-shadow: 0 10px 28px rgba(0,0,0,0.45);
    overflow: hidden;
  }
  .card-front {
    left: 150px;
    top: 56px;
    background: radial-gradient(circle at 55% 75%, var(--green-light), var(--green-deep) 75%);
    display: flex;
    align-items: center;
    justify-content: center;
  }
  .brand {
    display: flex;
    align-items: center;
    gap: 22px;
  }
  .brand-square {
    width: 58px;
    height: 58px;
    background: var(--paper);
    border-radius: 6px;
  }
  .brand-name {
    font-family: "Lato", sans-serif;
    font-weight: 400;
    font-size: 64px;
    color: var(--paper);
    letter-spacing: 1px;
  }
  .card-back {
    left: 450px;
    top: 420px;
    background: linear-gradient(135deg, var(--paper) 40%, var(--paper-shade));
    color: var(--green-ink);
  }
  .sales-photo {
    position: absolute;
    left: 32px;
    top: 108px;
    width: 96px;
    height: 120px;
    border-radius: 3px;
    background: linear-gradient(180deg, var(--photo-top), var(--photo-bottom));
    border: 2px solid var(--green-ink);
    box-sizing: border-box;
  }
  .contact-person {
    position: absolute;
    left: 146px;
    top: 116px;
  }
  .person-name {
    font-family: "Oswald", sans-serif;
    font-weight: 500;
    font-size: 36px;
    line-height: 1;
    margin: 0 0 8px;
    text-transform: uppercase;
    letter-spacing: -0.5px;
  }
  .person-line, .address-line {
    font-family: "Lato", sans-serif;
    font-size: 12px;
    line-height: 1.4;
    letter-spacing: 0.5px;
    text-transform: uppercase;
    margin: 0;
    white-space: nowrap;
  }
  .divider {
    position: absolute;
    left: 368px;
    top: 96px;
  }
  .contact-office {
    position: absolute;
    left: 400px;
    top: 116px;
  }
  .phone {
    font-family: "Oswald", sans-serif;
    font-weight: 500;
    font-size: 32px;
    line-height: 1.1;
    margin: 0 0 8px;
    letter-spacing: -0.5px;
  }
</style>
</head>
<body>
<div class="canvas">
  <section class="card card-front" aria-label="Card front">
    <div class="brand">
      <span class="brand-square"></span>
      <span class="brand-name">Fernvale</span>
    </div>
  </section>

  <section class="card card-back" aria-label="Card back">
    <div class="sales-photo" role="img" aria-label="Photo of the salesperson"></div>

    <div class="contact-person">
      <h1 class="person-name">Marcus Hale</h1>
      <p class="person-line">Chief Executive Officer</p>
      <p class="person-line">contact@fernvalehome.com</p>
      <p class="person-line">www.fernvalehome.com</p>
    </div>

    <svg class="divider" width="20" height="150" viewBox="0 0 20 150" aria-hidden="true">
      <line x1="4" y1="2" x2="14" y2="148" stroke="var(--green-ink)" stroke-width="3"/>
    </svg>

    <div class="contact-office">
      <p class="phone">555 01 234 56</p>
      <p class="address-line">14 East Ave, 3rd Floor,</p>
      <p class="address-line">Linden Court, Springfield</p>
      <p class="address-line">United States</p>
    </div>
  </section>
</div>
</body>
</html>
```